VoxMend needs a Letterhead

We need a letterhead for our company "VoxMend Consultants". Logo is attached. The company color is Turquoise. Icons for website, scan logo for website, icons for address, e-mail and phone appreciated rather than just words.

Industry/Entity Type

It Company

```html
<!DOCTYPE html>
<html lang="en">
<head>
<meta charset="utf-8">
<title>VoxMend Consultants — Letterhead</title>
<link rel="stylesheet" href="https://fonts.googleapis.com/css2?family=Arimo:wght@400;700&family=Great+Vibes&display=swap">
<style>
  :root {
    --brand-blue: #1a7bc4;
    --brand-green: #8cc63f;
    --ink: #333333;
    --paper: #ffffff;
    --footer-text: #ffffff;
  }
  html, body {
    margin: 0;
    padding: 0;
    overflow: hidden;
    background: var(--paper);
  }
  .letterhead {
    position: relative;
    width: 928px;
    height: 1200px;
    overflow: hidden;
    background: var(--paper);
    font-family: "Arimo", Arial, sans-serif;
    color: var(--ink);
  }
  .brand {
    position: absolute;
    left: 32px;
    top: 50px;
    display: flex;
    align-items: center;
    gap: 14px;
  }
  .brand-square {
    width: 44px;
    height: 44px;
    background: var(--brand-blue);
  }
  .brand-name {
    font-size: 30px;
    font-weight: 400;
    color: var(--brand-blue);
    letter-spacing: 0.2px;
  }
  .salutation {
    position: absolute;
    left: 83px;
    top: 232px;
    margin: 0;
    font-size: 16.5px;
  }
  .letter-body {
    position: absolute;
    left: 155px;
    top: 269px;
    width: 710px;
  }
  .letter-body p {
    margin: 0 0 20.5px;
    font-size: 16.2px;
    line-height: 20.5px;
  }
  .signature {
    position: absolute;
    left: 78px;
    top: 904px;
    margin: 0;
    font-family: "Great Vibes", cursive;
    font-size: 56px;
    color: #111111;
  }
  .signatory-title {
    position: absolute;
    left: 106px;
    top: 972px;
    margin: 0;
    font-size: 16px;
  }
  .footer {
    position: absolute;
    left: 70px;
    right: 0;
    top: 1128px;
    height: 72px;
    background: var(--brand-green);
    color: var(--footer-text);
    font-size: 15px;
    line-height: 21px;
  }
  .contact {
    position: absolute;
    top: 9px;
    display: flex;
    gap: 8px;
  }
  .contact svg { flex: none; }
  .contact-lines { display: flex; flex-direction: column; gap: 0; }
  .contact-row { display: flex; align-items: center; gap: 8px; }
  .contact--address { left: 56px; }
  .contact--phone { left: 302px; flex-direction: column; gap: 0; }
  .contact--web { left: 494px; flex-direction: column; gap: 0; }
</style>
</head>
<body>
<main class="letterhead">
  <header class="brand">
    <span class="brand-square"></span>
    <span class="brand-name">VoxMend Consultants</span>
  </header>

  <p class="salutation">Dear Sir / Madam,</p>

  <section class="letter-body">
    <p>Lorem ipsum dolor sit amet, consectetur adipisicing elit, sed do eiusmod tempor labore et olore magna aliqua. Ut enim ad minim veniam, quis nostrud exercitation ullamco laboris nisi ut aliquip ex ea commodo consequa.Lorem ipsum dolor sit amet, nsectetur adipisicing elit, sed do eiusmod tempor incididunt ut labore et dolore magna aliqua. Ut enim ad minim veniam, quis.</p>
    <p>Lorem ipsum dolor sit amet, consectetur adipisicing elit, sed do eiusmod tempor labore et dolore magna aliqua. Ut enim ad minim veniam, quis nostrud exercitation ullamco laboris nisi ut aliquip ex ea commodo consequa.Lorem ipsum dolor sit amet, nsectetur adipisicing elit, sed do eiusmod tempor incididunt ut labore et dolore magna aliqua. Ut enim ad minim veniam, quis.</p>
    <p>Lorem ipsum dolor sit amet, consectetur adipisicing elit, sed do eiusmod tempor labore et dolore magna aliqua. Ut enim ad minim veniam, quis nostrud exercitation ullamco laboris nisi ut aliquip ex ea commodo consequa.Lorem ipsum dolor sit amet, nsectetur adipisicing elit, sed do eiusmod tempor incididunt ut labore et dolore magna aliqua. Ut enim ad minim veniam, quis.</p>
    <p>Lorem ipsum dolor sit amet, consectetur adipisicing elit, sed do eiusmod tempor labore et dolore magna aliqua. Ut enim ad minim veniam, quis nostrud exercitation ullamco laboris nisi ut aliquip ex ea commodo consequa.Lorem ipsum dolor sit amet, nsectetur adipisicing elit, sed do eiusmod tempor incididunt ut labore et dolore magna aliqua. Ut enim ad minim veniam, quis.</p>
    <p>Lorem ipsum dolor sit amet, consectetur adipisicing elit, sed do eiusmod tempor labore et dolore magna aliqua. Ut enim ad minim veniam, quis nostrud exercitation ullamco laboris nisi ut aliquip ex ea commodo consequa.Lorem ipsum dolor sit amet, nsectetur adipisicing elit, sed do eiusmod tempor incididunt ut labore et dolore magna aliqua. Ut enim ad minim veniam, quis.</p>
  </section>

  <p class="signature">Your Name</p>
  <p class="signatory-title">Company Director</p>

  <footer class="footer">
    <div class="contact contact--address">
      <svg width="12" height="16" viewBox="0 0 12 16" aria-hidden="true"><path d="M6 0a6 6 0 0 0-6 6c0 4.5 6 10 6 10s6-5.5 6-10a6 6 0 0 0-6-6zm0 8.5A2.5 2.5 0 1 1 6 3.5a2.5 2.5 0 0 1 0 5z" fill="#fff"/></svg>
      <div class="contact-lines">
        <span>2718 Harbor Lane east,</span>
        <span>Millbrook, ST &nbsp;60482</span>
      </div>
    </div>
    <div class="contact contact--phone">
      <div class="contact-row">
        <svg width="14" height="14" viewBox="0 0 14 14" aria-hidden="true"><path d="M3 0.5 5 3.5 3.8 5a8 8 0 0 0 5.2 5.2L10.5 9l3 2-1.5 2.5C6 13.5.5 8 .5 2z" fill="#fff"/></svg>
        <span>000 000 00</span>
      </div>
      <div class="contact-row">
        <svg width="14" height="14" viewBox="0 0 14 14" aria-hidden="true"><rect x="3" y="0.5" width="8" height="13" rx="1.5" fill="#fff"/><rect x="4.5" y="2" width="5" height="8" fill="#8cc63f"/><circle cx="7" cy="11.8" r="0.8" fill="#8cc63f"/></svg>
        <span>000 000 00</span>
      </div>
    </div>
    <div class="contact contact--web">
      <div class="contact-row">
        <svg width="18" height="14" viewBox="0 0 18 14" aria-hidden="true"><rect x="1" y="3" width="16" height="10" fill="none" stroke="#fff" stroke-width="1.6"/><path d="M1 3l8 6 8-6M3 3 9 0l6 3" fill="none" stroke="#fff" stroke-width="1.6"/></svg>
        <span>name@voxmendconsultants.com</span>
      </div>
      <div class="contact-row">
        <svg width="18" height="16" viewBox="0 0 18 18" aria-hidden="true"><g fill="none" stroke="#fff" stroke-width="1.5"><circle cx="9" cy="9" r="7.5"/><ellipse cx="9" cy="9" rx="3.3" ry="7.5"/><path d="M1.5 9h15M3 5h12M3 13h12"/></g></svg>
        <span>www.voxmendconsultants.com</span>
      </div>
    </div>
  </footer>
</main>
</body>
</html>
```